Coffee and hot drinks advert on A-Board

Creative eye catching design to advertise coffee and hot drinks on an A-Board.

To use images and modern design to reflect the quality and almost specialist coffee house style drinks on offer.
We use organic milk and have had our own 'Larkfield Restaurant' coffee beans roasted to produce the perfect coffee.
We also use only the best hot chocolate and fresh cream to serve quality drinks.
All staff are barista trained.

Target Market(s)

Passing trade and coffee lovers for takeaway drinks

Industry/Entity Type

Coffee Shop

Font styles to use
Serif

Requirements
Must have
• Bold creative modern look.
• Independent coffee shop style look
• Mention we use 'Bramblewick Organic milk'
• We use our own roasted special blend of coffee
• speciality hot chocolate
Nice to have
• modern approach
• eye catching
Should not have
• complicated
• difficult to read
• old fashioned

```html
<!DOCTYPE html>
<html lang="en">
<head>
<meta charset="utf-8">
<title>Larkfield Restaurant – Takeaway Coffee A-Board</title>
<link href="https://fonts.googleapis.com/css2?family=Pinyon+Script&family=Vollkorn:wght@400;500;600&family=Oswald:wght@600&display=swap" rel="stylesheet">
<style>
  :root {
    --wall-light: #8d9684;
    --wall-dark: #3f4a3c;
    --gold-light: #f3d27a;
    --gold-mid: #d6a437;
    --gold-dark: #8a5d12;
    --mat: #c9a24a;
    --photo-brown: #5c2e1c;
    --photo-cream: #e9dcc8;
    --band: #582a1e;
    --cream: #f6e9c8;
    --orange: #e07f2c;
    --badge: #dc7a24;
    --white: #ffffff;
  }
  html, body {
    margin: 0;
    padding: 0;
    overflow: hidden;
    background: #ffffff;
  }
  .board {
    position: relative;
    width: 854px;
    height: 1200px;
    overflow: hidden;
    background: var(--band);
  }
  .wall {
    position: absolute;
    left: 0; top: 0;
    width: 854px; height: 759px;
    background: radial-gradient(ellipse at 40% 40%, var(--wall-light) 0%, #6b7563 55%, var(--wall-dark) 100%);
  }
  .frame {
    position: absolute;
    left: 54px; top: 30px;
    width: 742px; height: 682px;
    box-sizing: border-box;
    background: linear-gradient(135deg, var(--gold-light) 0%, var(--gold-mid) 40%, var(--gold-dark) 75%, var(--gold-mid) 100%);
    box-shadow: 0 10px 24px rgba(0,0,0,0.45);
  }
  .frame-mat {
    position: absolute;
    left: 88px; top: 98px;
    width: 566px; height: 484px;
    box-sizing: border-box;
    background: linear-gradient(160deg, #e7c56a, var(--mat) 50%, #a9812d);
    border: 4px solid var(--gold-dark);
  }
  .coffee-photo {
    position: absolute;
    left: 134px; top: 152px;
    width: 473px; height: 391px;
    background: radial-gradient(ellipse at 45% 45%, var(--photo-cream) 0%, #b07a4e 30%, var(--photo-brown) 60%, #3a1a10 100%);
    border: 3px solid var(--gold-dark);
    box-sizing: border-box;
  }
  .barista-badge {
    position: absolute;
    left: 637px; top: 587px;
    width: 172px; height: 172px;
    border-radius: 50%;
    background: var(--badge);
    border: 7px solid var(--white);
    box-sizing: border-box;
    display: flex;
    align-items: center;
    justify-content: center;
    box-shadow: 0 4px 10px rgba(0,0,0,0.35);
  }
  .barista-badge p {
    margin: 0;
    transform: rotate(-8deg);
    font-family: "Oswald", sans-serif;
    font-weight: 600;
    font-size: 26px;
    line-height: 27px;
    color: var(--cream);
    text-align: center;
    text-transform: uppercase;
  }
  .message {
    position: absolute;
    left: 0; top: 759px;
    width: 854px;
    text-align: center;
    font-family: "Vollkorn", serif;
  }
  .headline {
    margin: 38px 0 0;
    color: var(--cream);
    font-weight: 500;
    font-size: 53px;
    line-height: 58px;
  }
  .headline .initial {
    font-family: "Pinyon Script", cursive;
    font-size: 86px;
    font-weight: 400;
    line-height: 0;
  }
  .offer {
    margin: 12px 0 0;
    color: var(--orange);
    font-weight: 500;
    font-size: 27px;
    line-height: 38px;
  }
  .offer .house-name {
    display: block;
    font-size: 41px;
    line-height: 50px;
  }
  .speciality {
    margin: 20px 0 0;
    color: var(--white);
    font-weight: 600;
    font-size: 19px;
    line-height: 24px;
  }
</style>
</head>
<body>
  <main class="board">
    <div class="wall" role="img" aria-label="Textured sage green wall"></div>

    <div class="frame" role="img" aria-label="Ornate gilded gold picture frame">
      <div class="frame-mat"></div>
      <div class="coffee-photo" role="img" aria-label="Cappuccino with chocolate latte art in a white cup on a wooden table"></div>
    </div>

    <div class="barista-badge">
      <p>All<br>staff are<br>barista<br>trained</p>
    </div>

    <section class="message">
      <h1 class="headline"><span class="initial">M</span>asters in the art of<br>quality coffee to take away</h1>
      <p class="offer">Try our own
        <span class="house-name">Larkfield Restaurant</span>
        Roasted Coffee Beans with Bramblewick<br>Organic Milk to produce the perfect coffee</p>
      <p class="speciality">Discover the ultimate speciality Hot Chocolate with Fresh Cream</p>
    </section>
  </main>
</body>
</html>
```